Venbrisk Card

We want a business card that shows people who we are the log attached was designed by the designers on graft hive,we are using the OO in the logo (speech bubbles as our icon,so please make that part of the card ) keep the colouring the same as the logo design and we will be using high end production on the card using silver foil as the icon to make it stand out.
As Venbrisk we specialise in finding influencers through social networks for brands, so if you used yammo to comment about sports products and you were followed by of lot of users and interacted with those users then the algorithm finds you and we contact you to work for our clients as a company we then have a set of influencers that we use to support new sports products.
Also we use our algorithm to help athletes,models etc to be scored via there digital influence so when say Orvel QD ask me to find a skater that is not so much a podium rider but is more digital focused for a digital campaign then we work out who those guys or girls are to help Orvel QD
Venbrisk is the name of the product and company, However I just wanted to give you the rationale of why we chose venbrisk in the first place. Aldo itself is an 'abbreviation' from the proper name Aldemar Fusk from Keeper of the Vales. The character was able to look into the morvendal (sometimes translated as "Seeing Stone" but literally meaning "Farsighted" or "One that Sees from Afar") and see into the far corners of the Universe. Much in the same way as the platform has been developed is able to look into the far corners of the social network arena to help brands and Athletes will be able to see how they rated....but don't worry i don't go running around in the woods with a foam Axe and an army of dwarfs!!!
Digital Directors,Brand Directors,Athletes,Models,Celebrities and agents
Business

```html
<!DOCTYPE html>
<html lang="en">
<head>
<meta charset="utf-8">
<title>Venbrisk Business Card</title>
<link rel="stylesheet" href="https://fonts.googleapis.com/css2?family=Questrial&display=swap">
<style>
  :root {
    --page: #ffffff;
    --card-top: #2b2d31;
    --card-bottom: #1b1c1f;
    --brand-blue: #4ab4e8;
    --text-white: #f2f3f5;
    --silver-light: #f4f4f5;
    --silver-mid: #b9bbbf;
    --silver-dark: #6f7276;
    --divider: #9a9ca0;
  }
  * { box-sizing: border-box; margin: 0; padding: 0; }
  html, body {
    width: 1200px;
    height: 900px;
    overflow: hidden;
    background: var(--page);
    font-family: "Questrial", "Century Gothic", sans-serif;
  }
  .card {
    position: absolute;
    top: 260px;
    width: 573px;
    height: 332px;
    background: linear-gradient(180deg, var(--card-top), var(--card-bottom));
    overflow: hidden;
  }
  .card--front { left: 15px; }
  .card--back { left: 612px; }

  .front__wordmark {
    position: absolute;
    left: 0;
    top: 18px;
    width: 500px;
    text-align: center;
    font-size: 104px;
    line-height: 1;
    color: var(--brand-blue);
    letter-spacing: -2px;
  }
  .front__band {
    position: absolute;
    left: 0;
    top: 160px;
    width: 100%;
    height: 14px;
    background: linear-gradient(90deg, var(--silver-dark), var(--silver-light) 40%, var(--silver-mid) 70%, var(--silver-dark));
  }
  .front__person {
    position: absolute;
    right: 376px;
    top: 208px;
    text-align: right;
  }
  .front__name {
    font-size: 20px;
    color: var(--brand-blue);
    white-space: nowrap;
  }
  .front__role {
    font-size: 16px;
    color: var(--text-white);
    margin-top: 2px;
  }
  .front__divider {
    position: absolute;
    left: 218px;
    top: 187px;
    width: 1px;
    height: 106px;
    background: var(--divider);
  }
  .contact-list {
    position: absolute;
    left: 238px;
    top: 195px;
    list-style: none;
  }
  .contact-list__item {
    display: flex;
    align-items: center;
    height: 25.5px;
    font-size: 20px;
    color: var(--text-white);
    white-space: nowrap;
  }
  .contact-list__icon {
    width: 22px;
    height: 22px;
    margin-right: 8px;
    flex: none;
  }
  .contact-list__icon * { fill: none; stroke: var(--brand-blue); stroke-width: 2; stroke-linejoin: round; stroke-linecap: round; }
  .contact-list__icon .solid { fill: var(--brand-blue); stroke: none; }

  .back__mark {
    position: absolute;
    inset: 0;
    display: flex;
    align-items: center;
    justify-content: center;
    gap: 22px;
  }
  .back__dot {
    width: 58px;
    height: 58px;
    border-radius: 50%;
    background: var(--silver-mid);
  }
  .back__name {
    font-size: 92px;
    line-height: 1;
    color: var(--silver-mid);
    letter-spacing: -1px;
  }
</style>
</head>
<body>
  <section class="card card--front" aria-label="Card front">
    <h1 class="front__wordmark">venbrisk</h1>
    <div class="front__band"></div>
    <div class="front__person">
      <p class="front__name">Corin Halvey</p>
      <p class="front__role">Manager</p>
    </div>
    <div class="front__divider"></div>
    <ul class="contact-list">
      <li class="contact-list__item">
        <svg class="contact-list__icon" viewBox="0 0 24 24" aria-hidden="true"><path class="solid" d="M6 2l4 4-2.5 2.5a12 12 0 0 0 8 8L18 14l4 4-3 3C10 21 3 14 3 5z"/></svg>
        1800 472 318
      </li>
      <li class="contact-list__item">
        <svg class="contact-list__icon" viewBox="0 0 24 24" aria-hidden="true"><circle cx="12" cy="12" r="10"/><ellipse cx="12" cy="12" rx="4.5" ry="10"/><path d="M2 12h20M4 6.5h16M4 17.5h16"/></svg>
        www.venbrisk.com
      </li>
      <li class="contact-list__item">
        <svg class="contact-list__icon" viewBox="0 0 24 24" aria-hidden="true"><path class="solid" d="M2 9l10-7 10 7v13H2z"/><path d="M3 10l9 6 9-6" style="stroke:#1f2023"/></svg>
        info@venbrisk.com
      </li>
      <li class="contact-list__item">
        <svg class="contact-list__icon" viewBox="0 0 24 24" aria-hidden="true"><path class="solid" d="M12 2L1 12h3v10h6v-6h4v6h6V12h3z"/></svg>
        PO Box 2741 Harbour Plaza
      </li>
    </ul>
  </section>

  <section class="card card--back" aria-label="Card back">
    <div class="back__mark">
      <span class="back__dot"></span>
      <span class="back__name">venbrisk</span>
    </div>
  </section>
</body>
</html>
```